Willowmere Paws Gala Sponsor & Stallholder Leaflet Design

Willowmere Paws Gala is the updated and refreshed version of the Brackenfield Pup Fair (See www.brackenfieldpupfair.co.uk).
Under new management, we need a leaflet designed to promote the event to potential stallholders and sponsors.
Willowmere Paws Gala is a fun day out for dogs and their human companions, with a range of activities for both.
As this is an outdoor event, we would like this theme in the leaflet.
It is being held in the grounds of Ashcombe Hall - http://www.ashcombehall.com
Attached is the required copy.
Note:
Leaflet format of DL/6 page is preferred, but will accept A5/4page
I will require the final work in InDesign format
Target Market(s)
Dog owners and lovers
Industry/Entity Type
Event
Look and feel

```html
<!DOCTYPE html>
<html lang="en">
<head>
<meta charset="utf-8">
<title>Willowmere Paws Gala – Sponsors &amp; Exhibitors</title>
<link href="https://fonts.googleapis.com/css2?family=Baloo+2:wght@600;700&family=Raleway:wght@400;600;700&display=swap" rel="stylesheet">
<style>
:root{
  --leaf:#6ea83c;
  --leaf-mid:#5a9535;
  --forest:#0e4a25;
  --forest-deep:#0b3d1e;
  --ink:#1f4d1a;
  --sun:#ffc20e;
  --cream:#eef4dc;
  --white:#ffffff;
}
*{box-sizing:border-box;margin:0;padding:0}
html,body{width:1200px;height:842px;overflow:hidden;background:#fff}
.leaflet{position:relative;width:1200px;height:842px;overflow:hidden;background:var(--leaf);font-family:"Raleway",sans-serif;color:var(--cream)}
.panel{position:absolute;top:0;height:842px}
.panel--sponsor{left:0;width:392px;background:var(--leaf)}
.panel--trade{left:392px;width:382px;background:var(--leaf-mid)}
.panel--contact{left:774px;width:426px;background:var(--leaf)}
.ground{position:absolute;left:0;bottom:0;width:1200px;height:110px}
.abs{position:absolute}
.tag{position:absolute;height:36px;color:var(--ink);font-family:"Baloo 2",sans-serif;font-weight:700;font-size:25px;line-height:38px;text-align:center}
.tag svg{position:absolute;inset:0;width:100%;height:100%}
.tag span{position:relative}
.subhead{color:var(--ink);font-size:16px;font-weight:600}
.why{list-style:none;font-size:13px;font-weight:600;line-height:20px}
.why li{position:relative;padding-left:38px}
.why li::before{content:"";position:absolute;left:0;top:6px;width:8px;height:8px;background:var(--forest)}
.bar{position:absolute;background:var(--forest);color:var(--white);font-weight:700;display:flex;align-items:center;justify-content:center}
.lead{color:var(--ink);font-size:12.5px;font-weight:700;line-height:19px}
.perks{list-style:none;font-size:11px;font-weight:600;line-height:13px}
.perks li{position:relative;padding-left:16px;margin-bottom:6px}
.perks li::before{content:"";position:absolute;left:0;top:2px;width:9px;height:9px;background:var(--sun)}
.perks li.plain::before{display:none}
.perks--wide li{margin-bottom:11px}
.intro{color:var(--ink);font-size:12px;font-weight:700;line-height:16px}
.price{color:var(--cream);font-size:10.5px;font-weight:600;line-height:14px}
.price table{border-collapse:collapse}
.price td{padding:0 14px 0 0}
.price .head{color:var(--ink);font-weight:700}
.note{color:#2f6a22;font-size:8.5px;line-height:11px}
.guide td{font-size:10.5px;padding:0;line-height:14px}
.guide .num{text-align:right}
.body-copy{font-size:11px;font-weight:600;line-height:13.5px;color:var(--cream)}
.contact-title{color:var(--white);font-family:"Baloo 2",sans-serif;font-weight:700;font-size:23px;line-height:27px;letter-spacing:.3px}
.contact-row{position:absolute;left:808px;width:363px;height:46px;background:var(--forest);color:var(--white);font-weight:700;display:flex;align-items:center;gap:14px;padding-left:28px}
.contact-row svg{flex:none}
.photo{position:absolute;background:var(--white);padding:12px;box-shadow:0 3px 8px rgba(0,0,0,.25)}
.photo div{width:100%;height:100%}
.photo--dane{left:910px;top:380px;width:268px;height:250px;transform:rotate(9deg)}
.photo--dane div{background:linear-gradient(180deg,#5aa0e0 0%,#a9d2f2 55%,#6f8f3a 75%,#4f7a2a 100%)}
.photo--beagle{left:750px;top:500px;width:300px;height:270px;transform:rotate(-6deg)}
.photo--beagle div{background:linear-gradient(180deg,#4f7d2c 0%,#7aa844 45%,#8b6a3c 65%,#5c8a32 100%)}
</style>
</head>
<body>
<main class="leaflet">

  <section class="panel panel--sponsor">
    <div class="tag" style="left:0;top:23px;width:272px">
      <svg viewBox="0 0 272 36" preserveAspectRatio="none"><polygon points="0,0 258,0 272,18 258,36 0,36" fill="#ffc20e"/></svg>
      <span>Sponsorship</span>
    </div>
    <p class="subhead abs" style="left:62px;top:70px">Why sponsor</p>
    <ul class="why abs" style="left:72px;top:92px">
      <li>Give your brands or products</li>
      <li>exposure to circa 20,000 visitors</li>
      <li>&nbsp;Access a highly targeted market</li>
      <li>Lead generation</li>
      <li>&nbsp;Brand positioning</li>
      <li>Increase brand recognition</li>
    </ul>

    <div class="bar" style="left:30px;top:231px;width:321px;height:36px;font-size:15.5px">What Does Sponsorship Give You?</div>
    <p class="lead abs" style="left:34px;top:283px;width:330px">There are four types of sponsorship, dependant of your budget and marketing goals.</p>

    <div class="bar" style="left:27px;top:342px;width:148px;height:23px;font-size:12px">Main Event Sponsor</div>
    <ul class="perks abs" style="left:27px;top:390px;width:185px">
      <li>Branding on all media communications - leaflets, tickets, website, emails etc</li>
      <li>Large Exhibition Space</li>
      <li>Sign and Banner Rights across the event venue and rings (banner production included)</li>
      <li>Local, regional and national Media Exposure</li>
      <li class="plain">2 pages in the show guide</li>
      <li>Global Judging rights</li>
      <li>Massive Consumer Awareness</li>
      <li class="plain">20 Complimentary tickets</li>
    </ul>

    <div class="bar" style="left:222px;top:342px;width:148px;height:23px;font-size:12px">Ring Sponsor</div>
    <ul class="perks abs" style="left:222px;top:390px;width:150px">
      <li>Exhibition Space</li>
      <li>Joint Banner Rights in the event ring (banner production included)</li>
      <li>1 pages in the show guide</li>
      <li>Ring Judging rights</li>
      <li>5 Complimentary tickets</li>
    </ul>

    <div class="bar" style="left:222px;top:586px;width:148px;height:23px;font-size:12px">Gift/Sample Sponsor</div>
    <ul class="perks abs" style="left:222px;top:626px;width:150px">
      <li>Promote your brand or product by supplying gift or sample</li>
      <li>Data collection opportunity</li>
      <li>Exhibition Space</li>
      <li>1/2 page in the show guide</li>
    </ul>

    <div class="bar" style="left:30px;top:624px;width:148px;height:23px;font-size:12px">Competition Sponsor</div>
    <ul class="perks perks--wide abs" style="left:27px;top:661px;width:185px">
      <li>Exhibition Space</li>
      <li>1/2 page in the show guide</li>
      <li>Competition Judging rights</li>
      <li>2 Complimentary tickets</li>
    </ul>
  </section>

  <section class="panel panel--trade">
    <div class="tag" style="left:37px;top:23px;width:303px">
      <svg viewBox="0 0 303 36" preserveAspectRatio="none"><polygon points="14,0 289,0 303,18 289,36 14,36 0,18" fill="#ffc20e"/></svg>
      <span>Trade Exhibitors</span>
    </div>
    <p class="intro abs" style="left:36px;top:76px;width:305px">There are several space options available to exhibitors, both covered and grass space only. Covering the two days of the event, exhibitors also get a line listing in the event show guide and website.</p>

    <div class="price abs" style="left:36px;top:177px">
      <p class="head" style="margin-bottom:14px">Grass Space only</p>
      <table>
        <tr><td>3m(w) x 6m(d)</td><td>£150</td></tr>
        <tr><td>6m(w) x 10m(d)</td><td>£250</td></tr>
        <tr><td>9m(w) x 10m(d)</td><td>£350</td></tr>
        <tr><td>12m(w) x 10m(d)</td><td>£450</td></tr>
      </table>
    </div>
    <div class="price abs" style="left:200px;top:177px;width:160px">
      <p>Marquee Space - £15 per square meter<br>(minimum 6 square meters)</p>
      <p style="margin-top:14px">Power (Marquee Only) - £30 per 13amp Socket<br>Table (6' x 2'6") - £10 each</p>
    </div>

    <div class="note abs" style="left:36px;top:277px;width:310px">
      <p>Notes:</p>
      <p>All exhibitors must have valid and suitable public, product &amp; employee liability insurance</p>
      <p>All (human) food based exhibitors must have suitable food hygiene qualifications and certification</p>
    </div>

    <div class="bar" style="left:37px;top:358px;width:293px;height:23px;font-size:11px">Additional Marketing Opportunities</div>
    <p class="abs" style="left:37px;top:390px;color:var(--ink);font-size:9.5px;font-weight:700">Show Guide</p>
    <p class="note abs" style="left:37px;top:404px;width:300px">A minimum of 32 pages, the show guide not only contains useful features and stories, but also a full listing of all sponsors and exhibitors.</p>
    <div class="price abs" style="left:37px;top:438px">
      <table class="guide">
        <tr class="head"><td style="width:137px"></td><td style="width:70px">Exhibitor</td><td>Standard Advertiser</td></tr>
        <tr><td colspan="3" style="height:12px"></td></tr>
        <tr><td>Back cover</td><td class="num" style="padding-right:24px">£350</td><td class="num" style="padding-right:4px">£700</td></tr>
        <tr><td>Full page</td><td class="num" style="padding-right:24px">£250</td><td class="num" style="padding-right:4px">£500</td></tr>
        <tr><td>Half Page</td><td class="num" style="padding-right:24px">£135</td><td class="num" style="padding-right:4px">£270</td></tr>
        <tr><td>Quarter Page</td><td class="num" style="padding-right:24px">£75</td><td class="num" style="padding-right:4px">£150</td></tr>
        <tr><td>Sixth Page</td><td class="num" style="padding-right:24px">£50</td><td class="num" style="padding-right:4px">£100</td></tr>
      </table>
    </div>

    <div class="bar" style="left:40px;top:552px;width:293px;height:23px;font-size:11px">Promotional Voucher</div>
    <div class="body-copy abs" style="left:40px;top:591px;width:308px">
      <p>The centre of the guide will contain a pull out voucher booklet, with 6 vouchers per page. Exhibitors offering a special promotion, price or service during the event can promote it via a voucher, which will not only highlight the offer, but also identify the location of their stand.<br>This costs £50 per voucher</p>
      <p style="margin-top:14px">Banners in Competition Rings - £10 per meter (60cm high) - design &amp; production not included</p>
    </div>
  </section>

  <section class="panel panel--contact"></section>

  <svg class="ground" viewBox="0 0 1200 110" preserveAspectRatio="none" aria-hidden="true">
    <polygon points="0,75 400,70 800,45 1200,0 1200,110 0,110" fill="#0b4a22"/>
  </svg>

  <h2 class="contact-title abs" style="left:840px;top:28px;width:340px">To book or for more information contact the Willowmere Paws Gala team:</h2>

  <div class="contact-row" style="top:168px">
    <svg width="20" height="32" viewBox="0 0 20 32"><rect x="2" y="2" width="16" height="28" rx="3" fill="none" stroke="#ffc20e" stroke-width="3"/><rect x="6" y="7" width="8" height="7" fill="#ffc20e"/><circle cx="10" cy="24" r="2" fill="#ffc20e"/></svg>
    <span style="font-size:14.5px">01632 960481</span>
  </div>
  <div class="contact-row" style="top:230px">
    <svg width="32" height="22" viewBox="0 0 32 22"><rect x="1.5" y="1.5" width="29" height="19" fill="none" stroke="#ffc20e" stroke-width="3"/><polyline points="2,2 16,13 30,2" fill="none" stroke="#ffc20e" stroke-width="3"/><line x1="2" y1="20" x2="12" y2="11" stroke="#ffc20e" stroke-width="2.5"/><line x1="30" y1="20" x2="20" y2="11" stroke="#ffc20e" stroke-width="2.5"/></svg>
    <span style="font-size:13.5px">contact@willowmerepawsgala.co.uk</span>
  </div>
  <div class="contact-row" style="top:292px">
    <svg width="34" height="34" viewBox="0 0 34 34"><circle cx="16" cy="16" r="14" fill="#ffc20e"/><g fill="none" stroke="#0e4a25" stroke-width="2"><ellipse cx="16" cy="16" rx="6" ry="13"/><line x1="3" y1="16" x2="29" y2="16"/><line x1="5" y1="9" x2="27" y2="9"/><line x1="5" y1="23" x2="27" y2="23"/></g><polygon points="20,18 32,26 26,27 29,33 27,34 24,28 20,31" fill="#ffc20e" stroke="#0e4a25" stroke-width="1.2"/></svg>
    <span style="font-size:13.5px">www.willowmerepawsgala.co.uk</span>
  </div>

  <figure class="photo photo--dane"><div role="img" aria-label="Photo of a black Great Dane sitting on a grassy hill under a blue sky"></div></figure>
  <figure class="photo photo--beagle"><div role="img" aria-label="Photo of a beagle lying on a green lawn"></div></figure>

</main>
</body>
</html>
```